Business Card Design Project

Business card for new event planning company. I will load in 2 different colors of logs for you to use.

Target Market(s)

meeting planners and business leaders

Industry/Entity Type

Event Planning

Requirements
Must have
• memorable/ creative please - maybe logo on back of the card

Information for business card: (Information may change)

LaVonna Pettibrook
lav@MarigoldOccasionsandGalas.com
www.MarigoldOccasionsandGalas.com
613.275.9042
Nice to have
• Do you think it would be too much to add chirpy, QX, workmesh logo to card to connect?

all are LaVonna Pettibrook

```html
<!DOCTYPE html>
<html lang="en">
<head>
<meta charset="utf-8">
<title>Marigold Occasions &amp; Galas — Business Card</title>
<link href="https://fonts.googleapis.com/css2?family=EB+Garamond:wght@400;500&display=swap" rel="stylesheet">
<style>
  :root {
    --backdrop: #e9e6e1;
    --card-dark: #2a2628;
    --card-light: #f8f7f4;
    --orange: #f07a22;
    --lavender: #a5aadf;
    --ink: #2b2a2a;
    --rule: #4a4848;
  }
  * { margin: 0; padding: 0; box-sizing: border-box; }
  html, body {
    width: 1200px; height: 686px; overflow: hidden;
    background: var(--backdrop);
    font-family: "EB Garamond", Georgia, serif;
  }
  .stage {
    width: 1200px; height: 686px;
    display: flex; align-items: center; justify-content: center; gap: 70px;
  }
  .card {
    position: relative;
    box-shadow: 0 10px 28px rgba(0,0,0,0.18);
  }
  /* Front */
  .card-front {
    width: 540px; height: 308px;
    background: var(--card-dark);
  }
  .dot-motif {
    position: absolute; left: 42px; top: 40px;
    width: 200px; height: 150px;
    border-radius: 40px;
    background: linear-gradient(135deg, var(--orange) 0%, #c99197 50%, var(--lavender) 100%);
    opacity: 0.9;
  }
  .brand {
    position: absolute; right: 34px; bottom: 34px;
    display: flex; align-items: center; gap: 10px;
  }
  .brand-mark {
    width: 14px; height: 14px; border-radius: 50%;
    background: var(--orange);
  }
  .brand-name {
    color: var(--lavender);
    font-size: 26px; font-weight: 500;
    line-height: 1;
  }
  /* Back */
  .card-back {
    width: 308px; height: 540px;
    background: var(--card-light);
    color: var(--ink);
  }
  .card-back .brand {
    top: 30px; right: 26px; bottom: auto; gap: 7px;
  }
  .card-back .brand-mark { width: 9px; height: 9px; }
  .card-back .brand-name { font-size: 15px; }
  .holder {
    position: absolute; left: 40px; top: 168px; right: 34px;
  }
  .holder-name {
    font-size: 24px; font-weight: 400;
    padding-bottom: 14px;
  }
  .divider {
    border: 0; border-top: 1px solid var(--rule);
    margin: 0 0 14px 0;
  }
  .detail-list {
    list-style: none;
    font-size: 13px; line-height: 1.75;
    margin-bottom: 14px;
  }
</style>
</head>
<body>
<main class="stage">
  <section class="card card-front">
    <div class="dot-motif" role="img" aria-label="Pattern of orange and lavender dots"></div>
    <div class="brand">
      <span class="brand-mark"></span>
      <span class="brand-name">Marigold Occasions &amp; Galas</span>
    </div>
  </section>

  <section class="card card-back">
    <div class="brand">
      <span class="brand-mark"></span>
      <span class="brand-name">Marigold Occasions &amp; Galas</span>
    </div>
    <div class="holder">
      <h1 class="holder-name">LaVonna Pettibrook</h1>
      <hr class="divider">
      <ul class="detail-list">
        <li>E: lav@MarigoldOccasionsandGalas.com</li>
        <li>W: www.MarigoldOccasionsandGalas.com</li>
        <li>M: 613.275.9042</li>
      </ul>
      <hr class="divider">
      <ul class="detail-list">
        <li>Q: qx.com/LaVonna Pettibrook</li>
        <li>C: chirpy.com/LaVonna Pettibrook</li>
        <li>Wm: workmesh.com/LaVonna Pettibrook</li>
      </ul>
      <hr class="divider">
    </div>
  </section>
</main>
</body>
</html>
```